New Toothpaste brand needs a logo & packaging design

Our company is launching a new toothpaste and is looking for a logo and packaging design. The toothpaste brand is called Brivana. The packaging should have the same design quality as the major international brands, such as Lumora, Lumora Totalcare, Dentiva, Pexolo, Wind-rise, Marvest, etc. The dominant colors for our brand should be hues of blue, similar to other major brands. In addition, there should be a little bit of green to represent the "Fresh Mint Blast" flavor and the "Extracts of Aloe Vera" included in the ingredients.

There are typically 3 unique sides on a toothpaste box:

The face: Repeated on ~3 sides of the 4 faces of the box
The back: The 4th box face has the instructions for use, ingredients, company information, bar code/product info, and some branding elements.
The sides: Usually consisting of just the logo, flavor etc.

Please refer to existing brands such as Lumora, Lumora Total-care, and Dentiva for an example of typical box layout and elements.

Task Details:
Package Dimensions: 180 mm x 48 mm x 28 mm, 100 ml toothpaste tube
Brand Name: Brivana
Description: Fluoride Toothpaste
Flavor: Fresh Mint Blast
5 Actions: Protects against cavities and tartar, freshens breath, whitens teeth, and maintains healthy gums. These actions can also be made into a list like Lumora Total Care or Dentiva Max care. For instance, Strong Teeth, Fresh Breath, Whitening, Healthy Gums, Cavity and Tartar Protection.
Also contains whitening micro particles and extracts of aloe vera which may be highlighted on the package

Overall, the look should be high quality and with the same look and feel as the big brands mentioned previously. We do not have an existing logo for this brand. The face of the package is the most important element as it is often repeated on several sides and on the tube itself.

Please let me know if you have any questions.

I've attached some of our favorite big brand designs below. I would say the Lumora Total Care and Gleam vers

The logos I've seen so far for Brivana, have been a bit too bold. A little bold is okay, but just needs to be moderate. 

I would like the colors to be bright and appealing. I mentioned shades of blue being the major color, but green should also be highlighted as well, perhaps in a 80% blue to 20% green ratio. 

Target Market(s)

adult consumer of toothpaste, both female and male.

Industry/Entity Type

It Company

Requirements
Must have
• A logo with the brand name: Brivana
Description or sub text: Fluoride Toothpaste
Flavor: Fresh Mint Blast
A phrase or list describing the Toothpaste Actions: e.g., Protects against cavities and tartar, freshens breath, whitens teeth, and maintains healthy gums. Or as a list simialr to Lumora Total Care or Dentiva Max Care:
-Anti-cavity
-Anti-tartar
-Fresh breath
-Whitening
-Healthy Gums

Special ingredient of "whitening micro particles: and "extracts of aloe vera", which should also be highlighted.

The color should mostly be shades of blue, with only a little bit of green to accentuate the fresh mint blast flavor and aloe vera

Nice to have
• The design should really look good next to lumora total care, gleam pure, and dentiva max care. These are our favorite designs.
Should not have
• For aloe vera, there is no need to show the plant.

The Brivana logo shouldn't be too Bold. This should be appeal to all consumers, not just men.

```html
<!DOCTYPE html>
<html lang="en">
<head>
<meta charset="utf-8">
<title>Brivana Fluoride Toothpaste – Carton Dieline</title>
<link rel="stylesheet" href="https://fonts.googleapis.com/css2?family=Roboto:ital,wght@0,700;1,400;1,500&display=swap">
<style>
  :root {
    --navy-deep: #0a1f57;
    --navy: #0f2f7a;
    --royal: #1a56b0;
    --bright: #2a86dc;
    --sky: #3fb0ee;
    --mint: #8cc63f;
    --mint-light: #b4dc5a;
    --white: #ffffff;
    --fold: rgba(255,255,255,0.35);
    --brand-font: "Roboto", Arial, sans-serif;
  }
  html, body { margin: 0; padding: 0; overflow: hidden; background: var(--white); }
  .carton {
    position: relative;
    width: 1200px;
    height: 760px;
    overflow: hidden;
    background: var(--white);
    font-family: var(--brand-font);
    color: var(--white);
  }
  .dieline { position: absolute; inset: 0; }
  .brand {
    position: absolute;
    margin: 0;
    font-weight: 700;
    font-style: normal;
    letter-spacing: 0.02em;
    line-height: 1;
    color: var(--white);
    white-space: nowrap;
  }
  .descriptor {
    position: absolute;
    margin: 0;
    font-style: italic;
    font-weight: 500;
    white-space: nowrap;
  }
  .flavor-tab {
    position: absolute;
    display: flex;
    align-items: center;
    padding-left: 14px;
    box-sizing: border-box;
    background: var(--mint);
    box-shadow: 6px 6px 0 var(--mint-light);
    font-style: italic;
    font-weight: 500;
    white-space: nowrap;
  }
  .benefits {
    position: absolute;
    margin: 0;
    padding: 0;
    list-style: none;
    font-style: italic;
    font-weight: 500;
  }
  .benefits li { white-space: nowrap; }
  .claim {
    position: absolute;
    margin: 0;
    font-style: italic;
    font-weight: 500;
    font-size: 9.4px;
    letter-spacing: 0.14em;
    text-transform: uppercase;
    white-space: nowrap;
  }

  /* top panel */
  .top .brand { left: 255px; top: 76px; font-size: 40px; }
  .top .descriptor { left: 375px; top: 117px; font-size: 11px; }
  .top .flavor-tab { left: 825px; top: 40px; width: 148px; height: 28px; font-size: 14px; }
  .top .benefits { left: 622px; top: 54px; font-size: 12px; line-height: 14.4px; }

  /* face panels */
  .face .brand { font-size: 72px; }
  .face .descriptor { font-size: 15px; }
  .face .flavor-tab { width: 150px; height: 28px; font-size: 15px; }
  .face .benefits { font-size: 15px; line-height: 18px; }

  .face-main .brand { left: 282px; top: 220px; }
  .face-main .descriptor { left: 468px; top: 292px; }
  .face-main .flavor-tab { left: 825px; top: 158px; }
  .face-main .benefits { left: 806px; top: 204px; }
  .face-main .claim { left: 240px; top: 338px; }

  .face-lower .brand { left: 282px; top: 541px; }
  .face-lower .descriptor { left: 468px; top: 613px; }
  .face-lower .flavor-tab { left: 825px; top: 479px; }
  .face-lower .benefits { left: 806px; top: 525px; }
  .face-lower .claim { left: 240px; top: 659px; }

  .benefits li:nth-child(1) { padding-left: 24px; }
  .benefits li:nth-child(2) { padding-left: 20px; }
  .benefits li:nth-child(3) { padding-left: 16px; }
  .benefits li:nth-child(4) { padding-left: 12px; }
  .benefits li:nth-child(5) { padding-left: 8px; }
  .benefits li:nth-child(6) { padding-left: 4px; }

  /* end panels and tabs */
  .end-brand {
    position: absolute;
    font-weight: 700;
    font-size: 36px;
    line-height: 1;
    white-space: nowrap;
    transform-origin: center;
  }
  .end-left { left: 80px; top: 238px; transform: rotate(90deg); }
  .end-right { left: 965px; top: 238px; transform: rotate(-90deg); }
  .tab-brand {
    position: absolute;
    font-weight: 700;
    font-size: 11px;
    white-space: nowrap;
  }
  .tab-tl { left: 152px; top: 56px; transform: rotate(90deg); }
  .tab-bl { left: 152px; top: 410px; transform: rotate(90deg); }
  .tab-tr { left: 1000px; top: 66px; transform: rotate(-90deg); }
  .tab-br { left: 1000px; top: 420px; transform: rotate(-90deg); }
</style>
</head>
<body>
<div class="carton">
  <svg class="dieline" width="1200" height="760" viewBox="0 0 1200 760">
    <defs>
      <linearGradient id="panelFill" gradientUnits="userSpaceOnUse" x1="218" y1="0" x2="978" y2="0">
        <stop offset="0" stop-color="#0a1f57"/>
        <stop offset="0.45" stop-color="#123f94"/>
        <stop offset="0.72" stop-color="#1d68c6"/>
        <stop offset="1" stop-color="#3aaaea"/>
      </linearGradient>
      <linearGradient id="backFill" gradientUnits="userSpaceOnUse" x1="218" y1="0" x2="978" y2="0">
        <stop offset="0" stop-color="#0a1f57"/>
        <stop offset="0.6" stop-color="#113a8c"/>
        <stop offset="1" stop-color="#2a86dc"/>
      </linearGradient>
      <linearGradient id="endLeftFill" x1="0" y1="0" x2="1" y2="0">
        <stop offset="0" stop-color="#0f2f7a"/>
        <stop offset="1" stop-color="#0a1f57"/>
      </linearGradient>
      <linearGradient id="endRightFill" x1="0" y1="0" x2="1" y2="0">
        <stop offset="0" stop-color="#2a86dc"/>
        <stop offset="1" stop-color="#1a56b0"/>
      </linearGradient>
      <radialGradient id="glow">
        <stop offset="0" stop-color="#9fd8ff" stop-opacity="0.7"/>
        <stop offset="1" stop-color="#9fd8ff" stop-opacity="0"/>
      </radialGradient>
      <linearGradient id="streaks" x1="0" y1="0" x2="1" y2="0">
        <stop offset="0" stop-color="#5fc0f5" stop-opacity="0"/>
        <stop offset="0.5" stop-color="#5fc0f5" stop-opacity="0.35"/>
        <stop offset="1" stop-color="#5fc0f5" stop-opacity="0.1"/>
      </linearGradient>
    </defs>

    <!-- top flaps -->
    <polygon class="tab" points="115,55 150,18 218,18 218,150 150,150 115,118" fill="#0f2f7a"/>
    <polygon class="tab" points="978,18 1050,18 1085,55 1085,118 1050,150 978,150" fill="#1a56b0"/>
    <rect class="panel-top" x="218" y="18" width="760" height="137" fill="url(#panelFill)"/>

    <!-- end panels -->
    <path class="panel-end" d="M218,137 H70 Q18,137 18,190 V322 Q18,375 70,375 H218 Z" fill="url(#endLeftFill)"/>
    <path class="panel-end" d="M978,137 H1128 Q1180,137 1180,190 V322 Q1180,375 1128,375 H978 Z" fill="url(#endRightFill)"/>
    <circle cx="150" cy="256" r="70" fill="url(#glow)"/>
    <circle cx="1040" cy="256" r="70" fill="url(#glow)"/>

    <!-- main face -->
    <rect class="panel-face" x="218" y="155" width="760" height="203" fill="url(#panelFill)"/>
    <circle cx="380" cy="240" r="120" fill="url(#glow)" opacity="0.5"/>
    <rect role="img" aria-label="Soft light streak backdrop behind benefit list" x="700" y="160" width="260" height="190" fill="url(#streaks)"/>

    <!-- back panel and side tabs -->
    <polygon class="tab" points="115,380 218,380 218,492 150,492 115,455" fill="#0f2f7a"/>
    <polygon class="tab" points="978,380 1085,380 1085,455 1050,492 978,492" fill="#1a56b0"/>
    <rect class="panel-back" x="218" y="358" width="760" height="120" fill="url(#backFill)"/>
    <rect role="img" aria-label="Soft light streak backdrop on back panel" x="700" y="362" width="260" height="112" fill="url(#streaks)"/>
    <rect class="code-area" x="226" y="408" width="161" height="62" fill="#ffffff"/>

    <!-- lower face -->
    <rect class="panel-face" x="218" y="478" width="760" height="212" fill="url(#panelFill)"/>
    <circle cx="380" cy="560" r="120" fill="url(#glow)" opacity="0.5"/>
    <rect role="img" aria-label="Soft light streak backdrop behind benefit list" x="700" y="482" width="260" height="200" fill="url(#streaks)"/>

    <!-- glue flap -->
    <polygon points="200,690 240,690 245,745 215,745" fill="#0f2f7a"/>
    <polygon points="960,690 1000,690 985,745 960,745" fill="#2a86dc"/>
    <rect x="240" y="690" width="720" height="35" fill="#ffffff"/>
    <rect x="240" y="725" width="720" height="20" fill="#ffffff" stroke="#0f2f7a" stroke-width="1"/>

    <!-- glue strip and fold lines -->
    <rect x="960" y="18" width="18" height="727" fill="#3aaaea" opacity="0.45"/>
    <line x1="962" y1="18" x2="962" y2="745" stroke="#ffffff" stroke-width="1.2"/>
    <g stroke="var(--fold)" stroke-width="1" stroke-dasharray="4 3" fill="none">
      <line x1="218" y1="155" x2="978" y2="155"/>
      <line x1="218" y1="358" x2="978" y2="358"/>
      <line x1="218" y1="478" x2="978" y2="478"/>
      <line x1="218" y1="690" x2="978" y2="690"/>
      <line x1="218" y1="18" x2="218" y2="690"/>
      <line x1="978" y1="18" x2="978" y2="690"/>
      <line x1="100" y1="160" x2="100" y2="352"/>
      <line x1="1098" y1="160" x2="1098" y2="352"/>
    </g>
  </svg>

  <!-- top panel -->
  <section class="top">
    <p class="brand">BRIVANA</p>
    <p class="descriptor">Fluoride Toothpaste</p>
    <div class="flavor-tab">Fresh Mint Blast</div>
    <ul class="benefits">
      <li>Strong Teeth</li><li>Fresh Breath</li><li>Whitening</li>
      <li>Healthy Gums</li><li>Cavity Protection</li><li>Tartar Protection</li>
    </ul>
  </section>

  <!-- main face -->
  <section class="face face-main">
    <h1 class="brand">BRIVANA</h1>
    <p class="descriptor">Fluoride Toothpaste</p>
    <div class="flavor-tab">Fresh Mint Blast</div>
    <ul class="benefits">
      <li>Strong Teeth</li><li>Fresh Breath</li><li>Whitening</li>
      <li>Healthy Gums</li><li>Cavity Protection</li><li>Tartar Protection</li>
    </ul>
    <p class="claim">Especial ingredient of whitening micro particles and extracts of aloe vera, which should also be highlighted.</p>
  </section>

  <!-- lower face -->
  <section class="face face-lower">
    <p class="brand">BRIVANA</p>
    <p class="descriptor">Fluoride Toothpaste</p>
    <div class="flavor-tab">Fresh Mint Blast</div>
    <ul class="benefits">
      <li>Strong Teeth</li><li>Fresh Breath</li><li>Whitening</li>
      <li>Healthy Gums</li><li>Cavity Protection</li><li>Tartar Protection</li>
    </ul>
    <p class="claim">Especial ingredient of whitening micro particles and extracts of aloe vera, which should also be highlighted.</p>
  </section>

  <!-- ends and tabs -->
  <span class="end-brand end-left">BRIVANA</span>
  <span class="end-brand end-right">BRIVANA</span>
  <span class="tab-brand tab-tl">BRIVANA</span>
  <span class="tab-brand tab-bl">BRIVANA</span>
  <span class="tab-brand tab-tr">BRIVANA</span>
  <span class="tab-brand tab-br">BRIVANA</span>
</div>
</body>
</html>
```